Web page for organic mosquito control company in Texas

Looking for a webpage that communicates the three main objectives of the company: Guaranteed effective, Affordable Rates, Organic Solution.
The company specializes in safe organic mosquito control. Service is conducted monthly during the mosquito season. What makes Quillmoor unique is the fact that it does not employ heavy pesticides, expensive equipment purchases and no nozzles misting installed throughout the property. I have some videos that I want to integrate. Please specify what format and codec do want the multi media file in?
Target Market(s)
Mothers 30-55 years of age
Industry/Entity Type
It Company
Number of Pages Required
5+ page
Requirements
Must have
- Predominant space for video on the home page
Nice to have
- Environmental theme without overdoing it.

```html
<!DOCTYPE html>
<html lang="en">
<head>
<meta charset="utf-8">
<title>Quillmoor Mosquito Control System</title>
<link href="https://fonts.googleapis.com/css2?family=Open+Sans:wght@300;400;600;700&display=swap" rel="stylesheet">
<style>
  :root{
    --green:#84bd3a;
    --green-dark:#6fa52c;
    --green-band:#8dc24a;
    --ink:#2e2e2e;
    --muted:#8a8a8a;
    --nav:#383838;
    --nav-line:#2a2a2a;
    --panel:#f5f5f5;
    --footer:#2c2c2c;
    --white:#ffffff;
  }
  *{margin:0;padding:0;box-sizing:border-box}
  html,body{width:708px;height:1200px;overflow:hidden;background:var(--white)}
  body{position:relative;font-family:"Open Sans",Arial,sans-serif;color:var(--ink)}
  .abs{position:absolute}

  .top-rule{left:0;top:0;width:708px;height:2px;background:var(--green)}
  .brand{left:0;top:12px;width:708px;text-align:center;font-weight:700;font-size:17px;line-height:18px;color:var(--ink)}
  .brand small{display:block;font-size:6px;letter-spacing:4px;font-weight:600;line-height:10px;margin-top:2px}

  .hero-band{left:0;top:83px;width:708px;height:458px;
    background:radial-gradient(ellipse at 50% 40%,#b6d98a 0%,#93c558 45%,#6ea533 100%)}

  .main-nav{left:58px;top:69px;width:592px;height:36px;display:flex;background:var(--nav);box-shadow:0 3px 6px rgba(0,0,0,.25)}
  .main-nav a{display:flex;align-items:center;justify-content:center;color:var(--white);text-decoration:none;font-size:7.5px;font-weight:400;border-right:1px solid var(--nav-line)}
  .main-nav a.active{background:var(--green)}

  .slider{left:58px;top:122px;width:592px;height:379px;background:var(--white);box-shadow:0 6px 14px rgba(0,0,0,.3)}
  .slide-media{left:8px;top:8px;width:576px;height:324px;
    background:linear-gradient(180deg,#a9c86a 0%,#7fae3c 45%,#5f9128 100%)}
  .slide-dots{left:266px;top:300px;width:60px;height:24px;background:#eeeeee;display:flex;align-items:center;justify-content:center;gap:4px}
  .slide-dots i{width:8px;height:8px;border-radius:50%;background:#c9c9c9;box-shadow:inset 0 1px 2px rgba(0,0,0,.3)}
  .slide-dots i.on{background:#444}
  .slide-caption{left:0;top:343px;width:592px;text-align:center;font-size:14.5px;font-weight:600;color:#333;letter-spacing:.1px}
  .caption-mark{left:457px;top:339px;width:30px;height:30px}

  .feature{top:560px;width:190px;text-align:center}
  .feature .badge{width:80px;height:80px;border-radius:50%;background:var(--green);margin:0 auto;display:flex;align-items:center;justify-content:center}
  .feature h3{font-size:14.5px;font-weight:600;margin-top:13px;line-height:18px}
  .feature h4{font-size:14.5px;font-weight:300;line-height:20px}
  .feature p{font-size:7.2px;line-height:12px;color:var(--muted);margin-top:9px}
  .btn{display:inline-block;margin-top:10px;background:var(--nav);color:var(--white);font-size:7px;padding:0 9px;height:23px;line-height:23px;text-decoration:none}

  .about-band{left:0;top:800px;width:708px;height:232px;background:var(--panel);border-top:1px solid #e4e4e4}
  .hello{left:58px;top:827px;width:370px}
  .hello h2{font-size:14.5px;font-weight:400;line-height:20px}
  .hello h3{font-size:14.5px;font-weight:300;color:#555;line-height:20px;margin-top:5px}
  .hello .points{font-size:14px;font-weight:600;color:var(--green);margin-top:5px;line-height:20px}
  .hello .points span{color:var(--muted);font-weight:400}
  .hello p{font-size:7.2px;line-height:12px;color:var(--muted);margin-top:10px}
  .divider{left:458px;top:823px;width:1px;height:190px;background:#e2e2e2}
  .how{left:495px;top:826px;width:160px}
  .how h2{font-size:14.5px;font-weight:400;line-height:20px}
  .how ul{list-style:none;margin-top:7px}
  .how li{position:relative;padding:5px 0 7px 15px;font-size:8px;line-height:13.5px;color:var(--muted);border-bottom:1px solid #e6e6e6}
  .how li::before{content:"";position:absolute;left:0;top:8px;width:10px;height:10px;border-radius:50%;background:var(--green)}
  .how li::after{content:"";position:absolute;left:3px;top:11.5px;width:3px;height:3px;border-top:1.2px solid #fff;border-right:1.2px solid #fff;transform:rotate(45deg)}

  .partners{left:40px;top:1052px;width:628px;height:26px;display:flex;align-items:center;justify-content:space-between}
  .partners .arrow{width:7px;height:7px;border-left:1.5px solid #aaa;border-bottom:1.5px solid #aaa}
  .partners .prev{transform:rotate(45deg)}
  .partners .next{transform:rotate(-135deg)}
  .partners span.name{font-size:14px;font-weight:600;color:#6f6f6f;display:flex;align-items:center;gap:4px}
  .partners span.name i{width:12px;height:12px;background:#6f6f6f;border-radius:50%}

  .site-footer{left:0;top:1091px;width:708px;height:109px;background:var(--footer)}
  .foot-col{top:1117px}
  .foot-col h5{font-size:8px;font-weight:600;color:var(--green);line-height:10px;height:16px}
  .foot-col a{display:block;font-size:6.8px;color:#d6d6d6;text-decoration:none;line-height:12.7px}
  .social a{display:flex;align-items:center;gap:5px;line-height:17px}
  .social a i{width:12px;height:12px;border-radius:50%;background:#3d7ec9}
  .foot-brand{left:560px;top:1118px;width:90px;text-align:right;font-size:13px;font-weight:600;color:#777;line-height:14px}
  .copyright{left:500px;top:1158px;width:150px;text-align:right;font-size:6.5px;color:#cfcfcf}
</style>
</head>
<body>
  <div class="abs top-rule"></div>
  <div class="abs brand">Quillmoor<br>Mosquito<small>Control System</small></div>

  <div class="abs hero-band"></div>

  <nav class="abs main-nav">
    <a class="active" href="#" style="width:67px">HOME</a>
    <a href="#" style="width:68px">ABOUT US</a>
    <a href="#" style="width:74px">PROJECTS</a>
    <a href="#" style="width:84px">OUR TEAM</a>
    <a href="#" style="width:84px">HOW IT WORK</a>
    <a href="#" style="width:66px">SERVICES</a>
    <a href="#" style="width:67px">FEATURES</a>
    <a href="#" style="width:82px;border-right:0">CONTACT US</a>
  </nav>

  <section class="abs slider">
    <div class="abs slide-media" role="img" aria-label="Video or photo of children playing with a ball on a green lawn"></div>
    <div class="abs slide-dots"><i></i><i class="on"></i><i></i><i></i></div>
    <div class="abs slide-caption">WE ARE A &nbsp;MOSQUITO CONTROL COMPANY &nbsp; &nbsp; &nbsp;</div>
    <div class="abs caption-mark" role="img" aria-label="Small mosquito illustration" style="background:#dcdcdc;border-radius:50%"></div>
  </section>

  <div class="abs feature" style="left:52px">
    <div class="badge">
      <svg width="38" height="36" viewBox="0 0 38 36"><rect x="3" y="16" width="8" height="17" fill="#fff"/><path d="M13 16 L20 4 Q24 3 24 8 L22 14 L33 14 Q36 15 35 19 L32 31 Q31 33 28 33 L13 33 Z" fill="#fff"/></svg>
    </div>
    <h3>GUARANTEED</h3><h4>EFFECTIVE</h4>
    <p>Vivamus vel eros eget magna volutpat sagitt isul'faucibus nibh a magna tincidunt accumsan hdr erit nunc facillorem ipduisis urabitur et lib.</p>
    <a class="btn" href="#">READ MORE</a>
  </div>
  <div class="abs feature" style="left:259px">
    <div class="badge">
      <svg width="36" height="36" viewBox="0 0 36 36"><path d="M4 4 L17 4 L33 20 L20 33 L4 17 Z" fill="#fff"/><circle cx="11" cy="11" r="3" fill="#84bd3a"/></svg>
    </div>
    <h3>AFFORDABLE</h3><h4>RATES</h4>
    <p>Vivamus vel eros eget magna volutpat sagitt isul'faucibus nibh a magna tincidunt accumsan hdr erit nunc facillorem ipduisis urabitur et lib.</p>
    <a class="btn" href="#">READ MORE</a>
  </div>
  <div class="abs feature" style="left:466px">
    <div class="badge">
      <svg width="40" height="34" viewBox="0 0 40 34"><path d="M4 30 Q6 6 36 4 Q36 28 10 28 Z" fill="none" stroke="#fff" stroke-width="3.5"/><path d="M4 31 Q16 18 28 12" stroke="#fff" stroke-width="2.5" fill="none"/></svg>
    </div>
    <h3>ORGANIC</h3><h4>SOLUTION</h4>
    <p>Vivamus vel eros eget magna volutpat sagitt isul'faucibus nibh a magna tincidunt accumsan hdr erit nunc facillorem ipduisis urabitur et lib.</p>
    <a class="btn" href="#">READ MORE</a>
  </div>

  <div class="abs about-band"></div>
  <section class="abs hello">
    <h2>HELLO THERE!</h2>
    <h3>WELCOME TO QUILLMOOR MOSQUITO!!</h3>
    <div class="points"><span>1)</span> Effective <span>2)</span> Affordable <span>3)</span> Natural and <span>4)</span> Safe.</div>
    <p>Designed in Texas by Texans, specifically for Texas Mosquitoes, the Quillmoor Mosquito Control System is the first organically-based mosquito control system that eliminates both mosquitoes and the need for automatic mosquito misting systems.</p>
    <p>Our 99.5% organic solution not only minimizes your family's risk to harmful pathogens such as West Nile Virus, Chikungunya, and Eastern Equine Encephalitis, but it also reduces pesticide exposure by 95% compared to nozzle misting systems. &nbsp;Better yet, our customer's report the Quillmoor system is nearly twice as effective as expensive nozzle systems.</p>
  </section>
  <div class="abs divider"></div>
  <section class="abs how">
    <h2>HOW IT WORKS</h2>
    <ul>
      <li>Remedying Conducive Conditions to Prevent Egg, Larvae, and Pupae Development</li>
      <li>Eradication of adult mosquitoes</li>
      <li>Repelling adult mosquitoes</li>
      <li>Sterilizing mosquito larvae</li>
    </ul>
  </section>

  <div class="abs partners">
    <i class="arrow prev"></i>
    <span class="name"><i></i>Tunewave</span>
    <span class="name">Gridsoft</span>
    <span class="name">Snapfolio</span>
    <span class="name">framestock</span>
    <span class="name">Tilepay</span>
    <span class="name">Snapfolio</span>
    <i class="arrow next"></i>
  </div>

  <footer class="abs site-footer"></footer>
  <div class="abs foot-col" style="left:60px"><h5>COMPANY</h5><a href="#">Home</a><a href="#">About</a><a href="#">Press</a><a href="#">Advertise</a></div>
  <div class="abs foot-col" style="left:135px"><h5>&nbsp;</h5><a href="#">Investors</a><a href="#">Blog</a><a href="#">Careers</a><a href="#">Contact</a></div>
  <div class="abs foot-col" style="left:237px"><h5>WHO WE ARE</h5><a href="#">Help Center</a><a href="#">Urgent Enquiries</a><a href="#">FAQ</a><a href="#">Forum</a></div>
  <div class="abs foot-col" style="left:349px"><h5>WHAT WE DO</h5><a href="#">Help Center</a><a href="#">Urgent Enquiries</a><a href="#">FAQ</a><a href="#">Forum</a></div>
  <div class="abs foot-col social" style="left:462px"><h5>CONNECT US</h5><a href="#"><i></i>Friendline</a><a href="#"><i></i>Chirpnet</a></div>
  <div class="abs foot-brand">Quillmoor<br>Mosquito</div>
  <div class="abs copyright">Copyright © 2015 Quillmoor Mosquito</div>
</body>
</html>
```